Renewed electronic office supplies

I need a landing page design for a B2B business that will sell refurbished and renewed electronic devices such as smartphones, laptops, tablets and other gadgets. We want to become suppliers of these devices to companies that need computers and other devices for their employees. The point of our business is that they can get a great device that is in very good contrition instead of buying brand new. Companies will be able to save 50-60% on these renewed devices. Not only that we will also buy the companies old devices which they no longe needs and renew them and give them new life so we can resell it.

Our services will be:

- sale of renewed devices with lifetime warranty

- purchase of old devices

- swap solution: meaning client buy from us and sell at the same time so we deduct the amount sale of their old devices into their purchase.

Some useful information:

- company name and logo are still pending

- we aim to provide all business with top quality of renewed and environmentally friendly electronics, while maintaining a minimal impact on the natural environment.

I have attached a word document with some additional info that might be useful

Looking forward to seeing all your great designs!

P.s. Please feel free to make designs that are not based on my documents also, we need different layouts and designs. as for now I see many of the designs are more or less the same. we need more variation on design

Target Market(s)

Medium to large Businesses

Industry/Entity Type

Technology Equipment

Requirements
Must have
• we need more designs to be submitted , 50 designs minimum

```html
<!DOCTYPE html>
<html lang="en">
<head>
<meta charset="utf-8">
<title>Renovo Device – Renewed Electronic Office Supplies</title>
<link href="https://fonts.googleapis.com/css2?family=Poppins:wght@400;500;600;700&display=swap" rel="stylesheet">
<style>
:root{
  --navy:#13294f;
  --navy-deep:#0f2243;
  --yellow:#f6b91a;
  --yellow-soft:#fcd45a;
  --ink:#1d2b45;
  --muted:#6b7384;
  --light:#eef0f3;
  --white:#ffffff;
}
*{margin:0;padding:0;box-sizing:border-box}
html,body{width:1200px;height:2496px;overflow:hidden}
body{font-family:'Poppins',sans-serif;color:var(--ink);background:var(--white);position:relative}

/* header */
.site-header{position:absolute;left:0;top:0;width:1200px;height:70px;background:var(--white);z-index:3}
.brand{position:absolute;left:40px;top:18px;font-weight:700;font-size:26px;color:var(--navy);display:flex;align-items:center;gap:10px}
.brand-dot{width:14px;height:14px;border-radius:50%;background:var(--yellow)}
.header-phone{position:absolute;right:40px;top:22px;display:flex;align-items:center;gap:10px;font-weight:600;font-size:16px;color:var(--navy)}

/* hero */
.hero{position:absolute;left:0;top:70px;width:1200px;height:650px;background:linear-gradient(180deg,#f3f4f6,#e9ebee);overflow:hidden}
.hero-circle{position:absolute;left:640px;top:-10px;width:560px;height:560px;border-radius:50%;background:var(--yellow)}
.hero-devices{position:absolute;left:580px;top:90px;width:520px;height:340px;border-radius:14px;background:linear-gradient(135deg,#2b2f38,#5a6070 60%,#9aa1ae)}
.hero-title{position:absolute;left:96px;top:180px;font-size:44px;line-height:1.2;font-weight:600;color:var(--navy);width:470px}
.hero-text{position:absolute;left:96px;top:310px;width:380px;font-size:15px;line-height:1.6;color:var(--muted)}
.btn{display:inline-block;background:var(--yellow);color:var(--white);font-weight:600;font-size:14px;border-radius:4px;padding:10px 22px}
.hero .btn{position:absolute;left:96px;top:436px}
.slider-dots{position:absolute;left:150px;top:584px;display:flex;gap:10px;align-items:center;color:var(--muted);font-size:14px}
.slider-dots i{display:block;width:12px;height:12px;border-radius:50%;background:#c6cad2}
.slider-dots i.on{background:var(--navy)}
.hero-social{position:absolute;right:88px;top:574px;display:flex;gap:12px}
.social{width:30px;height:30px;border-radius:50%;background:var(--yellow)}

/* what we do */
.what-we-do{position:absolute;left:0;top:720px;width:1200px;height:480px;background:var(--navy)}
.section-title{font-weight:700;font-size:40px;line-height:1.2;color:var(--white)}
.section-title em{font-style:normal;color:var(--yellow)}
.what-we-do .section-title{position:absolute;left:84px;top:56px}
.what-we-do .section-title::after{content:"";display:block;width:60px;height:3px;background:var(--yellow);margin-top:4px}
.what-we-do .section-sub{position:absolute;left:84px;top:128px;font-size:13px;color:#b9c3d6}
.category{position:absolute;width:200px;text-align:center}
.cat-visual{width:130px;height:130px;margin:0 auto;border-radius:50%;background:var(--white);position:relative;overflow:hidden}
.cat-visual.gold{background:var(--yellow)}
.cat-visual .shot{position:absolute;inset:24px;border-radius:10px;background:linear-gradient(135deg,#26303f,#6d7585)}
.cat-label{margin-top:18px;font-size:15px;color:var(--white);display:flex;justify-content:center;align-items:center;gap:8px}
.cat-label b{width:16px;height:16px;border:1.5px solid var(--yellow);border-radius:50%;display:inline-block}

/* about */
.phones-visual{position:absolute;left:150px;top:1300px;width:400px;height:480px;border-radius:30px;background:linear-gradient(135deg,#0e1d3a,#3a6fb4 45%,#d9dde3 55%,#b63d6b)}
.timeline-line{position:absolute;left:640px;top:1320px;height:440px;border-left:2px dashed #c4c9d2}
.step-icon{position:absolute;left:620px;width:42px;height:42px;border-radius:50%;background:var(--white);border:2px solid #d4d8df;display:flex;align-items:center;justify-content:center}
.step{position:absolute;left:690px;width:380px}
.step .eyebrow{font-size:14px;color:var(--muted);margin-bottom:6px}
.step h3{font-size:26px;line-height:1.25;font-weight:600;color:var(--navy)}
.step h3 em{font-style:normal;color:var(--yellow)}
.step p{font-size:11.5px;line-height:1.6;color:var(--muted);margin-top:10px}

/* services */
.service-pill{position:absolute;top:1920px;width:240px;height:140px;border-radius:70px;background:var(--yellow);color:var(--white);text-align:center;display:flex;flex-direction:column;align-items:center;justify-content:center;gap:10px;font-size:13px;font-weight:600;line-height:1.35;padding:0 34px}

/* cta band */
.cta-band{position:absolute;left:0;top:2140px;width:1200px;height:54px;background:var(--light);display:flex}
.cta-band a{flex:1;display:flex;align-items:center;justify-content:center;gap:12px;font-size:19px;font-weight:500;color:var(--navy);text-decoration:none}

/* footer */
.site-footer{position:absolute;left:0;top:2220px;width:1200px;height:276px;background:var(--navy);color:var(--white)}
.site-footer .brand{left:72px;top:28px;color:var(--white);font-size:24px}
.footer-col{position:absolute;top:34px;font-size:12.5px;line-height:2;color:#c2cbdb}
.footer-col h4{font-size:15px;font-weight:500;color:var(--white);margin-bottom:8px}
.newsletter-label{position:absolute;left:112px;top:80px;font-size:14px}
.newsletter{position:absolute;left:72px;top:108px;width:210px;height:30px;background:var(--white);border-radius:15px;font-size:11px;color:var(--muted);padding:7px 14px}
.newsletter span{position:absolute;right:3px;top:3px;height:24px;width:52px;border-radius:12px;background:var(--yellow);color:var(--white);font-size:11px;text-align:center;line-height:24px}
.footer-social{position:absolute;left:100px;top:158px;display:flex;gap:12px}
.contact-row{display:flex;gap:10px;align-items:flex-start}
.contact-row svg{flex:none;margin-top:6px}
.copyright{position:absolute;left:0;bottom:14px;width:100%;text-align:center;font-size:12px;color:var(--yellow)}
</style>
</head>
<body>

<header class="site-header">
  <div class="brand"><span>Renovo Device</span><span class="brand-dot"></span></div>
  <div class="header-phone">
    <svg width="22" height="22" viewBox="0 0 24 24"><path fill="#13294f" d="M6.6 10.8a15 15 0 0 0 6.6 6.6l2.2-2.2a1 1 0 0 1 1-.25 11.4 11.4 0 0 0 3.6.6 1 1 0 0 1 1 1V20a1 1 0 0 1-1 1A17 17 0 0 1 3 4a1 1 0 0 1 1-1h3.5a1 1 0 0 1 1 1c0 1.25.2 2.45.6 3.6a1 1 0 0 1-.25 1z"/></svg>
    +1 (555) 010 2468
  </div>
</header>

<section class="hero">
  <div class="hero-circle"></div>
  <div class="hero-devices" role="img" aria-label="Laptop, tablet and smartphones showing colourful photo galleries"></div>
  <h1 class="hero-title">Reusable Electronic Office Supplies</h1>
  <p class="hero-text">We aim to provide all business with top quality of renewed and environmentally friendly electronics, while maintaining a minimal impact on the natural environment.</p>
  <span class="btn">Learn More</span>
  <div class="slider-dots">‹ <i class="on"></i><i></i><i></i> ›</div>
  <div class="hero-social"><span class="social"></span><span class="social"></span><span class="social"></span></div>
</section>

<section class="what-we-do">
  <h2 class="section-title">What We <em>Do</em></h2>
  <p class="section-sub">Our range of refurbished and renewed devices for work</p>
  <div class="category" style="left:120px;top:190px"><div class="cat-visual"><div class="shot" role="img" aria-label="Smartphone"></div></div><div class="cat-label">Smartphones <b></b></div></div>
  <div class="category" style="left:380px;top:220px"><div class="cat-visual"><div class="shot" role="img" aria-label="Laptop"></div></div><div class="cat-label">Laptops <b></b></div></div>
  <div class="category" style="left:640px;top:190px"><div class="cat-visual"><div class="shot" role="img" aria-label="Tablet"></div></div><div class="cat-label">Tablets <b></b></div></div>
  <div class="category" style="left:900px;top:190px"><div class="cat-visual gold"><div class="shot" role="img" aria-label="Wireless earbuds gadget"></div></div><div class="cat-label">Gadgets <b></b></div></div>
</section>

<div class="phones-visual" role="img" aria-label="Two smartphones, one with a cracked screen and one renewed"></div>
<div class="timeline-line"></div>

<div class="step-icon" style="top:1316px"><svg width="20" height="20" viewBox="0 0 24 24"><rect x="6" y="3" width="12" height="18" rx="2" fill="none" stroke="#13294f" stroke-width="2"/></svg></div>
<div class="step" style="top:1300px">
  <div class="eyebrow">We Are</div>
  <h3>A Smarter Circular Solution For Electronic <em>Supplies</em></h3>
  <p>Millions of devices are retired every year while still in good working order. We inspect, repair and renew them so your teams get reliable hardware at a fraction of the price, and fewer electronics end up in landfill. It is a simple, circular way to equip a growing business.</p>
</div>

<div class="step-icon" style="top:1548px"><svg width="20" height="20" viewBox="0 0 24 24"><path d="M3 5h3l2 10h10l2-7H7" fill="none" stroke="#13294f" stroke-width="2"/></svg></div>
<div class="step" style="top:1546px">
  <h3>Buy Reusable <em>IT</em></h3>
  <p>We specialise in refurbished devices with top quality for affordable prices. Each unit passes a full test and cleaning process before it ships to your office.</p>
</div>

<div class="step-icon" style="top:1680px"><svg width="20" height="20" viewBox="0 0 24 24"><path d="M4 12l5 5L20 6" fill="none" stroke="#13294f" stroke-width="2"/></svg></div>
<div class="step" style="top:1678px">
  <h3>Sell Your IT <em>Safely</em></h3>
  <p>We can take your used devices and make sure they get reused and given a new life. By selling us your old devices you lower costs and cut electronic waste.</p>
</div>

<div class="service-pill" style="left:250px">
  <svg width="34" height="34" viewBox="0 0 24 24"><path d="M4 9h14l-3-3M20 15H6l3 3" fill="none" stroke="#fff" stroke-width="2"/></svg>
  Swap Solution
</div>
<div class="service-pill" style="left:510px">
  <svg width="34" height="34" viewBox="0 0 24 24"><path d="M12 3l7 3v6c0 4-3 7-7 9-4-2-7-5-7-9V6z" fill="none" stroke="#fff" stroke-width="2"/></svg>
  Sale of Renewed Device with Lifetime Warranty
</div>
<div class="service-pill" style="left:770px">
  <svg width="34" height="34" viewBox="0 0 24 24"><path d="M2 6h12v10H2zM14 10h4l4 4v2h-8" fill="none" stroke="#fff" stroke-width="2"/><circle cx="6" cy="18" r="2" fill="#fff"/><circle cx="18" cy="18" r="2" fill="#fff"/></svg>
  Purchase Of Old Devices
</div>

<nav class="cta-band">
  <a>Sell to Us <svg width="24" height="12" viewBox="0 0 24 12"><path d="M0 6h22M17 1l5 5-5 5" fill="none" stroke="#13294f" stroke-width="1.6"/></svg></a>
  <a>Buy From Us <svg width="24" height="12" viewBox="0 0 24 12"><path d="M0 6h22M17 1l5 5-5 5" fill="none" stroke="#13294f" stroke-width="1.6"/></svg></a>
</nav>

<footer class="site-footer">
  <div class="brand"><span>Renovo Device</span><span class="brand-dot"></span></div>
  <div class="newsletter-label">Stay In Touch</div>
  <div class="newsletter">Enter Email<span>Send</span></div>
  <div class="footer-social"><span class="social"></span><span class="social"></span><span class="social"></span></div>

  <div class="footer-col" style="left:400px">
    <h4>Services</h4>
    <div>Smartphones</div><div>Laptops</div><div>Tablets</div><div>Gadgets</div>
  </div>
  <div class="footer-col" style="left:620px">
    <h4>Business</h4>
    <div>Buy From Us</div><div>Sell to Us</div><div>Partner Login</div><div>Our Shipping System</div><div>Terms of Sales</div>
  </div>
  <div class="footer-col" style="left:880px;width:260px">
    <h4>Get in Touch</h4>
    <div class="contact-row"><svg width="12" height="12" viewBox="0 0 24 24"><path fill="#f6b91a" d="M6.6 10.8a15 15 0 0 0 6.6 6.6l2.2-2.2a1 1 0 0 1 1-.25 11.4 11.4 0 0 0 3.6.6 1 1 0 0 1 1 1V20a1 1 0 0 1-1 1A17 17 0 0 1 3 4a1 1 0 0 1 1-1h3.5a1 1 0 0 1 1 1c0 1.25.2 2.45.6 3.6a1 1 0 0 1-.25 1z"/></svg>+1 (555) 010 2468</div>
    <div class="contact-row"><svg width="12" height="12" viewBox="0 0 24 24"><rect x="2" y="5" width="20" height="14" fill="none" stroke="#f6b91a" stroke-width="2"/><path d="M2 5l10 8 10-8" fill="none" stroke="#f6b91a" stroke-width="2"/></svg>hello@renovodevice.example</div>
    <div class="contact-row"><svg width="12" height="12" viewBox="0 0 24 24"><path fill="#f6b91a" d="M12 2a7 7 0 0 0-7 7c0 5 7 13 7 13s7-8 7-13a7 7 0 0 0-7-7zm0 9.5A2.5 2.5 0 1 1 12 6.5a2.5 2.5 0 0 1 0 5z"/></svg><span>Harbor Street 12, Northvale<br>Mon - Fri 09:00 - 17:00</span></div>
  </div>
  <div class="copyright">Renovo Device · 2024 All rights reserved</div>
</footer>

</body>
</html>
```